meditation/yoga retreat eco village ashram commune website

There is a group of 20-30 people living in the jungle of mexico. We all came together from all walks of life to help built a paradise on earth. This is a meditation ashram resort that is built by a living enlightenment master, a modern day buddha master Swami Veleth Tarunai. It's his vision and his love that he wants to share to the world.

The eco village project is on a 19 hectares forest land with a cenote (natural pond) as the heart centre surrounded by beautiful tropical gardens. This unique village is conceived in a mystical mayan circle as an oasis for creative arts crafts music and dance, mayan wisdom, eastern ayurveda, yoga, vipassana, meditation and silent retreat for the science of inner transformation this eco development will offer residents and visitors the experience of nature, silence, tranquility, meditativeness and a compassionate space for growth and flowering of human consciousness.

we are creating an inner science mystery school where we will offer ancient mayan traditions, buddhist vipassana, tibetan teachings, yoga, patanjali yoga, pranayama, we will also offer meditations and therapies like mystic rose, born again, no mind, painting group, breath, prana healing, primal, work as meditation all therapies and meditations will be offered for free we accept donations out of gratitude

The NEW DOMAIN for this website will be - www.VELMIRAKA.example

This is our old website - http://tarunaiveleth.example/o/miraka/
it is outdated and we haven't done anything to it in the past 5 years. Now that we are about to open to the world, we want a fresh new look that will captivate our audience. Please take a moment to browse our website to get an idea of who we are.

Also please check out our facebook page, you will see all our past events, upcoming events with pics and videos.
www.facebook.com/velmiraka
www.instagram.com/velmiraka

We have 3 festivals coming up, they are as follows.
Yoga festival - https://www.facebook.com/events/5203917264803159/
Art festival - https://www.facebook.com/events/5209384617250436/
Thai massage - https://www.facebook.com/events/6480215937402951/

Do not use any of the pictures from the old website, it is outdated, most are just drawings and sketches. I have zipped up some great pictures for you to use, ...also feel free to use anything from facebook/instagram as well.

For menu, also we will have sub-categories menu for each as well.

HOME
NEWS
THE PROJECT
EVENTS
VIDEOS
PHOTOS
TICKETS
RESIDENTIAL
DONATE
CONTACT

Things to include for main page.
*Upcoming Events
*Previous Pics/Videos of Past Events (grab them from our facebook page)
*Show some great construction building, moon palapa, star palapa, welcome center, etc..
*Maybe a section where the master can say a message.
*Mediation/Yoga section
*Residential Booking
*Facebook page, *twitter feed, instagram, youtube channel
Updates

Target Market(s)

meditation, yoga, art, dance festivals

Industry/Entity Type

Group

Number of Pages Required

1 page

Requirements
Must have
• we are looking for something classy, elegant, yet simple...stay away from traditional, give it a really cool modern touch.

```html
<!DOCTYPE html>
<html lang="en">
<head>
<meta charset="utf-8">
<title>Miraka — Meditation Ashram Eco Village</title>
<link rel="stylesheet" href="https://fonts.googleapis.com/css2?family=Open+Sans:ital,wght@0,300;0,400;0,600;0,700;1,400&display=swap">
<style>
:root{
  --red:#d3262c;
  --ink:#222;
  --text:#555;
  --muted:#8a8a8a;
  --band:#e4e4e4;
  --white:#fff;
  --dark:#2d2d2d;
  --nav:rgba(20,14,8,.72);
}
*{margin:0;padding:0;box-sizing:border-box}
html,body{width:1200px;height:3797px;overflow:hidden}
body{font-family:"Open Sans",Arial,sans-serif;color:var(--ink);background:var(--white);position:relative}
.abs{position:absolute}

/* hero */
.hero{left:0;top:0;width:1200px;height:610px;
  background:
    linear-gradient(180deg,rgba(30,12,4,0) 0,rgba(30,12,4,0) 72%,rgba(38,16,5,.85) 86%,#1c0b03 100%),
    radial-gradient(circle at 600px 90px,#fff6c8 0,#ffd35a 70px,#f3a51d 190px,#c7680f 360px,#7a3a0a 560px,#2e1605 760px);}
.sidebar{left:86px;top:0;width:172px;height:610px;background:var(--nav)}
.logo{left:86px;top:0;width:172px;height:157px;background:#0e0e0e;display:flex;align-items:center;justify-content:center;gap:10px}
.logo-mark{width:14px;height:14px;border-radius:50%;background:var(--red)}
.logo-name{color:var(--white);font-weight:700;font-size:24px;letter-spacing:2px}
.nav-rule{left:86px;top:165px;width:172px;height:4px;background:var(--red)}
.nav{left:111px;top:176px;list-style:none}
.nav li{font-size:12px;line-height:41.3px;color:var(--white);text-transform:uppercase}
.nav li.active{color:var(--red)}
.social{left:956px;top:36px;display:flex;gap:12px}
.social span{width:28px;height:28px;border-radius:50%;border:2px solid rgba(255,255,255,.9)}
.dots{left:568px;top:569px;display:flex;gap:14px}
.dots span{width:12px;height:12px;border-radius:50%;background:#9a9a9a}
.dots span.on{background:var(--red)}

/* news */
.news{left:0;top:610px;width:1200px;height:507px;background:#d9d9d9}
.news-panel{left:86px;top:610px;width:1028px;height:507px;background:var(--white)}
.section-title{left:0;top:676px;width:1200px;text-align:center;font-size:26px;font-weight:600}
.title-rule{top:697px;height:1px;background:#aaa;width:220px}
.news-item{top:778px;width:300px;text-align:center}
.date{width:116px;height:116px;border-radius:50%;background:#b3b3b3;margin:0 auto;color:var(--white);padding-top:28px;line-height:1}
.date b{font-size:28px;color:var(--ink);font-weight:700}
.date sup{font-size:13px;color:var(--ink);font-weight:600}
.date small{display:block;font-size:16px;margin-top:4px}
.news-item h3{color:var(--red);font-size:16px;font-weight:700;margin-top:44px;text-transform:uppercase}
.news-item p{font-size:13px;color:var(--text);line-height:21px;margin-top:8px;padding:0 18px}
.read{font-size:13px;font-weight:700;color:var(--ink);margin-top:10px;display:block}

/* events */
.events-title{left:0;top:1188px;width:1200px;text-align:center;color:var(--red);font-size:44px;font-weight:300}
.card{top:1332px;width:327px;height:486px;border:1px solid #ddd;background:var(--white);text-align:center}
.card-photo{margin:20px 20px 0;height:210px}
.card h3{color:var(--red);font-size:27px;font-weight:400;margin-top:20px;line-height:34px}
.card h4{font-size:27px;font-weight:300;color:#444;line-height:34px}
.card .rule{width:80px;height:2px;background:#f0b9bb;margin:14px auto 10px}
.card p{font-size:12px;color:var(--muted);line-height:17px;padding:0 38px}
.btn-outline{display:inline-block;margin-top:26px;border:1px solid var(--red);border-radius:20px;font-size:10px;font-weight:600;padding:8px 18px;color:#333;text-transform:uppercase}
.arrows{left:568px;top:1851px;display:flex;gap:8px}
.arrows svg{width:28px;height:28px}

/* master */
.master{left:0;top:1937px;width:1200px;height:311px;background:var(--band)}
.master-photo{left:190px;top:1952px;width:240px;height:282px;background:radial-gradient(ellipse at 50% 50%,#c9a48a 0,#b7b7b7 42%,var(--band) 70%)}
.master-copy{left:499px;top:1986px;width:540px}
.master-copy h2{font-size:22px;font-weight:400}
.master-copy h5{font-size:15px;font-style:italic;font-weight:400;color:#444;margin-top:14px;text-transform:uppercase}
.master-copy p{font-size:13.5px;color:var(--muted);line-height:23px;margin-top:12px}
.btn-pill{display:inline-block;margin-top:22px;border:1px solid #bbb;background:var(--white);border-radius:22px;font-size:11px;padding:12px 30px;color:#333;text-transform:uppercase}

/* welcome */
.welcome-h{top:2332px;font-size:27px;font-weight:300}
.welcome-h strong{color:var(--red);font-weight:700}
.place-h{top:2340px;font-size:19px;font-weight:400;color:var(--red);text-transform:uppercase}
.place-photo{top:2398px;height:316px}
.place-text{top:2738px;font-size:13px;color:var(--text);line-height:22px}
.place-text .read{color:var(--red);margin-top:12px}

/* gallery */
.gallery{left:0;top:2907px;width:1200px;height:456px}
.tile{position:absolute}

/* videos */
.videos{left:0;top:3363px;width:1200px;height:364px;background:#e8e8e8}
.video{left:86px;top:3413px;width:544px;height:177px;background:linear-gradient(180deg,#8fb6b0,#d9c9a8 55%,#c9b79c)}
.video-bar{left:86px;top:3566px;width:544px;height:24px;background:rgba(0,0,0,.85)}
.video-copy{left:681px;top:3418px;width:420px}
.video-copy h2{color:var(--red);font-size:28px;font-weight:400}
.video-copy p{font-size:14px;color:var(--text);line-height:21px;margin-top:16px}
.btn-dark{display:inline-block;margin-top:22px;background:#333;color:var(--white);border-radius:16px;font-size:10px;padding:8px 20px;text-transform:uppercase}

/* footer */
.footer{left:0;top:3727px;width:1200px;height:70px;background:var(--dark);color:var(--white);font-size:13px}
.footer .left{position:absolute;left:86px;top:26px}
.footer .right{position:absolute;right:86px;top:26px;color:#888}
</style>
</head>
<body>

<section>
  <div class="abs hero" role="img" aria-label="Photo of a woman meditating in lotus pose on a rock against the setting sun"></div>
  <div class="abs sidebar"></div>
  <div class="abs logo"><span class="logo-mark"></span><span class="logo-name">MIRAKA</span></div>
  <div class="abs nav-rule"></div>
  <ul class="abs nav">
    <li class="active">Home</li><li>News</li><li>The Project</li><li>Events</li><li>Videos</li>
    <li>Photos</li><li>Tickets</li><li>Residential</li><li>Donate</li><li>Contact</li>
  </ul>
  <div class="abs social" aria-label="Social links"><span></span><span></span><span></span><span></span></div>
  <div class="abs dots"><span></span><span class="on"></span><span></span></div>
</section>

<section>
  <div class="abs news"></div>
  <div class="abs news-panel"></div>
  <div class="abs title-rule" style="left:300px"></div>
  <div class="abs title-rule" style="left:680px"></div>
  <h2 class="abs section-title">OUR NEWS</h2>
  <article class="abs news-item" style="left:159px">
    <div class="date"><b>22</b><sup>nd</sup><small>SEP</small></div>
    <h3>Curabitur Tempor</h3>
    <p>Pellentesque enim erat, malesuada eu facilisis a, rutrum nec velit. Duis tincidunt imperdiet.</p>
    <span class="read">Read More+</span>
  </article>
  <article class="abs news-item" style="left:448px">
    <div class="date"><b>22</b><sup>nd</sup><small>SEP</small></div>
    <h3>Curabitur Tempor</h3>
    <p>Pellentesque enim erat, malesuada eu facilisis a, rutrum nec velit. Duis tincidunt imperdiet.</p>
    <span class="read">Read More+</span>
  </article>
  <article class="abs news-item" style="left:772px">
    <div class="date"><b>22</b><sup>nd</sup><small>SEP</small></div>
    <h3>Curabitur Tempor</h3>
    <p>Pellentesque enim erat, malesuada eu facilisis a, rutrum nec velit. Duis tincidunt imperdiet.</p>
    <span class="read">Read More+</span>
  </article>
</section>

<section>
  <h2 class="abs events-title">Up Coming Events</h2>
  <article class="abs card" style="left:86px">
    <div class="card-photo" role="img" aria-label="Women practising yoga in a class" style="background:linear-gradient(135deg,#e9c9a6,#c9825c 60%,#8a5a3c)"></div>
    <h3>Yoga</h3><h4>Events</h4><div class="rule"></div>
    <p>Duis vitae blandit nunc. Vestibulum molestie pharetra augue ac sodales. Etiam sodales augue euismod diam efficitur,</p>
    <span class="btn-outline">Know More</span>
  </article>
  <article class="abs card" style="left:438px">
    <div class="card-photo" role="img" aria-label="Young woman painting at an art table" style="background:linear-gradient(135deg,#6b5a4a,#c79a78 50%,#ddd1b0)"></div>
    <h3>Art</h3><h4>Events</h4><div class="rule"></div>
    <p>Duis vitae blandit nunc. Vestibulum molestie pharetra augue ac sodales. Etiam sodales augue euismod diam efficitur,</p>
    <span class="btn-outline">Know More</span>
  </article>
  <article class="abs card" style="left:790px">
    <div class="card-photo" role="img" aria-label="Woman receiving a Thai massage with flowers" style="background:linear-gradient(135deg,#f2ece4,#c68f6c 55%,#7a4a33)"></div>
    <h3>Thai massage</h3><h4>Events</h4><div class="rule"></div>
    <p>Duis vitae blandit nunc. Vestibulum molestie pharetra augue ac sodales. Etiam sodales augue euismod diam efficitur,</p>
    <span class="btn-outline">Know More</span>
  </article>
  <div class="abs arrows">
    <svg viewBox="0 0 28 28"><circle cx="14" cy="14" r="12.5" fill="#fff" stroke="#999"/><path d="M16 9l-5 5 5 5" fill="none" stroke="#555" stroke-width="1.6"/></svg>
    <svg viewBox="0 0 28 28"><circle cx="14" cy="14" r="12.5" fill="#fff" stroke="#999"/><path d="M12 9l5 5-5 5" fill="none" stroke="#555" stroke-width="1.6"/></svg>
  </div>
</section>

<section>
  <div class="abs master"></div>
  <div class="abs master-photo" role="img" aria-label="Woman seated in meditation pose"></div>
  <div class="abs master-copy">
    <h2>OUR MASTER MESSAGE</h2>
    <h5>Duis vitae blandit nunc vestibulum molestie pharetra</h5>
    <p>Nunc mollis turpis vitae augue hendrerit, a sodales quam<br>consectetur. Suspendisse sagittis elit in facilisis pellentesque. Morbi sit<br>amet dapibus nulla. Vestibulum ex ligula, tempor porta</p>
    <span class="btn-pill">View All</span>
  </div>
</section>

<section>
  <h2 class="abs welcome-h" style="left:86px">Welcome to <strong>MIRAKA</strong></h2>
  <h3 class="abs place-h" style="left:628px">Moon Palapa</h3>
  <h3 class="abs place-h" style="left:884px">Star Palapa</h3>
  <div class="abs place-photo" style="left:86px;width:504px;background:linear-gradient(180deg,#e8e6e2,#cfcac2 50%,#a9a49b)" role="img" aria-label="White welcome hall with chandelier and a seated statue"></div>
  <div class="abs place-photo" style="left:620px;width:241px;background:radial-gradient(circle at 50% 50%,#e7b56e,#c98f5a 40%,#6f8fa6 75%,#8a8a7a)" role="img" aria-label="Mosaic floor of the Moon Palapa"></div>
  <div class="abs place-photo" style="left:876px;width:238px;background:linear-gradient(180deg,#5c7a45,#3f6233 50%,#2e4a26)" role="img" aria-label="Star Palapa roof seen from above in the jungle"></div>
  <div class="abs place-text" style="left:86px;width:504px">Cras posuere enim nec nisl volutpat posuere. Pellentesque enim erat, malesuada eu facilisis a, rutrum nec velit. Duis tincidunt imperdiet orci sit amet sagittis. Sed luctus lectus quis lobortis<span class="read">Read More+</span></div>
  <div class="abs place-text" style="left:620px;width:241px">Nullam hendrerit, dui ut varius vulputate, tortor odio dapibus mi, et bibendum libero<span class="read">Read More+</span></div>
  <div class="abs place-text" style="left:876px;width:238px">Nullam hendrerit, dui ut varius vulputate, tortor odio dapibus mi, et bibendum libero<span class="read">Read More+</span></div>
</section>

<section class="abs gallery" aria-label="Photos of past events and buildings">
  <div class="tile" style="left:0;top:0;width:250px;height:223px;background:linear-gradient(160deg,#7a6a52,#c48a52 50%,#4c5a36)" role="img" aria-label="Palapa roof and garden"></div>
  <div class="tile" style="left:250px;top:0;width:270px;height:223px;background:radial-gradient(circle,#e2b97c,#b88a68 45%,#6d8aa0 80%)" role="img" aria-label="Mosaic floor"></div>
  <div class="tile" style="left:520px;top:0;width:265px;height:223px;background:linear-gradient(180deg,#3a3424,#6a5a3c 60%,#2e3a22)" role="img" aria-label="Open palapa pavilion"></div>
  <div class="tile" style="left:785px;top:0;width:160px;height:223px;background:linear-gradient(160deg,#b84a2e,#6f7a3a 60%,#3f4a2a)" role="img" aria-label="Red painted building"></div>
  <div class="tile" style="left:945px;top:0;width:255px;height:223px;background:linear-gradient(180deg,#8aa07a,#5f7a44 50%,#3c522c)" role="img" aria-label="Garden with carved mask"></div>
  <div class="tile" style="left:0;top:223px;width:155px;height:233px;background:linear-gradient(180deg,#3e5a34,#7a8a5a 60%,#4a5a3a)" role="img" aria-label="Jungle path"></div>
  <div class="tile" style="left:155px;top:223px;width:265px;height:233px;background:radial-gradient(circle at 50% 60%,#d0b890,#b04a30 40%,#7a3424)" role="img" aria-label="Round doorway in red wall"></div>
  <div class="tile" style="left:420px;top:223px;width:260px;height:233px;background:linear-gradient(160deg,#c9563a,#8a4a30 55%,#4a3a2a)" role="img" aria-label="Colourful interior with furniture"></div>
  <div class="tile" style="left:680px;top:223px;width:270px;height:233px;background:linear-gradient(180deg,#6a5638,#a48a5c 50%,#cfc6b0)" role="img" aria-label="Palapa ceiling interior"></div>
  <div class="tile" style="left:950px;top:223px;width:250px;height:233px;background:linear-gradient(180deg,#4a6a3a,#9a9a88 60%,#b8b4a4)" role="img" aria-label="Stone path to round gateway"></div>
</section>

<section>
  <div class="abs videos"></div>
  <div class="abs video" role="img" aria-label="Video of a teacher sitting in meditation before a mural"></div>
  <div class="abs video-bar"></div>
  <svg class="abs" style="left:96px;top:3571px" width="60" height="14" viewBox="0 0 60 14"><path d="M2 2v10M6 2v10" stroke="#fff" stroke-width="2"/><path d="M20 2l8 5-8 5z" fill="#fff"/><path d="M38 4h4l4-3v12l-4-3h-4z" fill="#fff"/></svg>
  <div class="abs video-copy">
    <h2>Videos</h2>
    <p>Duis vitae blandit nunc. Vestibulum molestie pharetra augue ac sodales. Etiam sodales augue euismod diam efficitur, at elementum neque faucibus. In dapibus tellus ut pharetra sagittis</p>
    <span class="btn-dark">View All</span>
  </div>
</section>

<footer class="abs footer">
  <span class="left">Residential Booking</span>
  <span class="right">© 2016 vel miraka. all reserved</span>
</footer>

</body>
</html>
```